Unique Business Card Design

Unique Business Card design for our orthotic and prosthetic company. Our logo is on our website, color is light blue. Unique shape (artificial leg shaped, vertical, etc..) preferred. Logo, business name, individual name and basic demographics needed.

Industry/Entity Type

Business

Contact Information for Business Card

Logo, Industry, Phone # Logo, "Prosthetic & Orthotic Services" Place to add individual name and contact info

Colors
cee9f5

Requirements
Must have
• The icon must be there, placement of "Prosthetic & Orthotic Services" can be moved
Nice to have
• Like the mix of light blue, and a little darker blue. One design included the icons from my website which was a nice touch

```html
<!DOCTYPE html>
<html lang="en">
<head>
<meta charset="utf-8">
<title>Stridewell Inc. – Business Card</title>
<link href="https://fonts.googleapis.com/css2?family=Arimo:wght@400&family=Tinos:ital@1&display=swap" rel="stylesheet">
<style>
  :root {
    --backdrop: #e6e6e6;
    --card: #fbfbfb;
    --brand-blue: #1764b0;
    --ink: #1c1c1c;
  }
  html, body {
    margin: 0;
    padding: 0;
    width: 1054px;
    height: 1200px;
    overflow: hidden;
    background: var(--backdrop);
  }
  .canvas {
    position: relative;
    width: 1054px;
    height: 1200px;
  }
  .card {
    position: absolute;
    top: 215px;
    width: 440px;
    height: 770px;
    background: var(--card);
    box-shadow: 0 6px 18px rgba(0,0,0,0.12);
    overflow: hidden;
  }
  .card--front { left: 62px; }
  .card--back { left: 552px; }

  .brand {
    position: absolute;
    left: 48px;
    top: 70px;
    width: 340px;
  }
  .brand__dot {
    display: block;
    width: 100px;
    height: 100px;
    border-radius: 50%;
    background: var(--brand-blue);
  }
  .brand__name {
    display: block;
    margin-top: 12px;
    font-family: "Arimo", Arial, sans-serif;
    font-weight: 400;
    font-size: 34px;
    line-height: 1.1;
    letter-spacing: 0.5px;
    color: var(--brand-blue);
    white-space: nowrap;
  }
  .brand__rule {
    display: block;
    margin-top: 8px;
    width: 320px;
    height: 4px;
    background: var(--brand-blue);
  }
  .tagline {
    position: absolute;
    left: 60px;
    top: 262px;
    font-family: "Tinos", "Times New Roman", serif;
    font-style: italic;
    font-size: 25px;
    color: var(--brand-blue);
    white-space: nowrap;
  }

  .contact {
    position: absolute;
    left: 168px;
    top: 380px;
    font-family: "Arimo", Arial, sans-serif;
    color: var(--ink);
    font-size: 21px;
    line-height: 1.3;
  }
  .contact p { margin: 0 0 30px; }
  .contact__name {
    font-size: 27px;
    line-height: 1.15;
  }

  .back-mark {
    position: absolute;
    right: 56px;
    bottom: 150px;
    width: 190px;
    height: 190px;
    border-radius: 50%;
    background: var(--brand-blue);
  }
</style>
</head>
<body>
<main class="canvas">
  <section class="card card--front" aria-label="Business card front">
    <div class="brand">
      <span class="brand__dot"></span>
      <span class="brand__name">STRIDEWELL INC.</span>
      <span class="brand__rule"></span>
    </div>
    <div class="tagline">Prosthetic &amp; Orthotic Services</div>

    <div class="contact">
      <p>
        <span class="contact__name">Miriam Halpern</span><br>
        Orthotist / Prosthetist<br>
        845-555-0142
      </p>
      <p>
        718-555-0190<br>
        hello@stridewell.net<br>
        www.stridewell.com
      </p>
      <p>
        1520 Maple Row<br>
        Brooklyn, NY 11299
      </p>
    </div>
  </section>

  <section class="card card--back" aria-label="Business card back">
    <span class="back-mark"></span>
  </section>
</main>
</body>
</html>
```